Cutting Edge Ultra High End Investment Company & Business Card

We are an Ultra High End PRIVATE Investment Group that is known for being ULTRA EXCLUSIVE and High NET WORTH. We are kind of the Meridian Vault Onyx for the private investment space in Orange County California, we only invite new investors by referral only.
We are looking for a information only web site that has a big impact once we invite new investors to our site. It needs to be Ultra Modern, Sophisticated, and make an impact. The only contact information that will be listed on the web site is a place where if invite a new investor they can enter a code to unlock access to our members contacts (future page)
We are like the look of a full size web lay out where it has a very large full screen image background.
We are open to any fonts any colors and any designs.
Target Market(s)
Private investors for information only
Industry/Entity Type
Business
Contact Information for Business Card
Please see attached jpeg. this is a very GENERIC
Number of Pages Required
1 page
Requirements
Must have
- Modern, Cutting Edge, Big Impact
Nice to have
- All the info that currently on VR Business Card Attached
Should not have
- Boxing gloves

```html
<!DOCTYPE html>
<html lang="en">
<head>
<meta charset="UTF-8">
<title>VR Private Investment Group</title>
<link rel="stylesheet" href="https://fonts.googleapis.com/css2?family=Open+Sans:wght@400;600;700;800&display=swap">
<style>
  :root {
    --page: #f1f1f1;
    --ink: #222222;
    --muted: #777777;
    --dark-band: #2e2e2e;
    --footer: #3a3a3a;
    --white: #ffffff;
    --nav-glass: rgba(255, 255, 255, 0.55);
  }
  * { margin: 0; padding: 0; box-sizing: border-box; }
  html, body { width: 745px; height: 1200px; overflow: hidden; }
  body {
    background: var(--page);
    font-family: "Open Sans", Arial, sans-serif;
    color: var(--ink);
    position: relative;
  }
  .hero {
    position: absolute; left: 0; top: 0; width: 745px; height: 400px;
    background:
      radial-gradient(circle at 82% 68%, #fbe3a4 0%, #e9a85a 12%, rgba(160,110,70,0) 40%),
      linear-gradient(180deg, #3d5466 0%, #6f7b80 40%, #9a8b78 70%, #4a4644 100%);
  }
  .nav-panel {
    position: absolute; left: 117px; top: 0; width: 516px; height: 119px;
    background: var(--nav-glass);
  }
  .brand {
    position: absolute; left: 0; right: 0; top: 18px;
    text-align: center; font-size: 40px; font-weight: 800; color: var(--ink);
    letter-spacing: 2px; line-height: 1;
  }
  .main-nav {
    position: absolute; left: 0; right: 0; top: 92px;
    display: flex; justify-content: space-around; padding: 0 20px;
    font-size: 8.5px; font-weight: 600; color: var(--ink); letter-spacing: 0.3px;
  }
  .hero-title {
    position: absolute; left: 117px; top: 165px;
    font-size: 47px; font-weight: 700; line-height: 1.16; color: var(--white);
    letter-spacing: 1px;
  }
  .slider-dots {
    position: absolute; left: 577px; top: 374px; display: flex; gap: 6px;
  }
  .slider-dots span { width: 7px; height: 7px; border-radius: 50%; background: var(--white); opacity: 0.9; }
  .slider-dots span + span { opacity: 0.6; }
  .pillar-band {
    position: absolute; left: 0; top: 400px; width: 745px; height: 151px;
    background: var(--dark-band);
  }
  .pillar {
    position: absolute; top: 430px; height: 121px;
    color: var(--white); text-align: center;
  }
  .pillar h2 { font-size: 24px; font-weight: 700; margin-top: 28px; letter-spacing: 0.5px; }
  .pillar p { font-size: 7.5px; line-height: 1.35; padding: 4px 16px 0; }
  .pillar-vision { left: 117px; width: 164px; background: linear-gradient(160deg, #2b3a48, #5a7084 60%, #1f2a33); }
  .pillar-mission { left: 296px; width: 161px; background: linear-gradient(160deg, #8a8e92, #454b52 60%, #1e2125); }
  .pillar-strategy { left: 472px; width: 161px; background: linear-gradient(160deg, #0c2a5c, #1e5ab0 55%, #0a1e44); }
  .news-grid { position: absolute; left: 117px; top: 608px; width: 516px; height: 497px; }
  .tile { position: absolute; }
  .photo-desert { left: 0; top: 0; width: 337px; height: 237px;
    background: linear-gradient(180deg, #3b1d16 0%, #9a3b1c 35%, #e48a3a 60%, #c8702e 75%, #6a3318 100%); }
  .photo-road { left: 337px; top: 162px; width: 179px; height: 75px;
    background: linear-gradient(180deg, #9fc2e4 0%, #d8e6f0 45%, #6f8f52 60%, #454848 100%); }
  .photo-portrait { left: 0; top: 237px; width: 156px; height: 223px;
    background: linear-gradient(180deg, #b8b8b8 0%, #8a8a8a 45%, #2b2f38 70%, #1b1e24 100%); }
  .photo-car { left: 156px; top: 373px; width: 181px; height: 87px;
    background: linear-gradient(180deg, #f4f4f4 0%, #dcdcdc 55%, #a9a9a9 100%); }
  .photo-night { left: 337px; top: 237px; width: 179px; height: 223px;
    background: radial-gradient(circle at 35% 40%, #f2c36a 0%, rgba(180,110,40,0.5) 18%, rgba(0,0,0,0) 40%),
      linear-gradient(180deg, #0d0d12 0%, #1e1a18 55%, #6a4a2a 80%, #1a1412 100%); }
  .news-card { background: var(--white); padding: 16px 13px 0; }
  .news-card h3 { font-size: 9px; font-weight: 700; margin-bottom: 8px; letter-spacing: 0.2px; }
  .news-card p { font-size: 7px; line-height: 1.45; color: var(--muted); }
  .news-meta { display: flex; gap: 26px; margin-top: 12px; font-size: 6.5px; color: var(--muted); }
  .news-card-top { left: 337px; top: 0; width: 179px; height: 162px; }
  .news-card-mid { left: 156px; top: 237px; width: 181px; height: 136px; padding-top: 22px; }
  .browse-bar {
    position: absolute; left: 0; top: 460px; width: 516px; height: 37px;
    background: var(--dark-band); color: var(--white);
    font-size: 8.5px; font-weight: 600; letter-spacing: 1.5px;
    display: flex; align-items: center; justify-content: center;
  }
  .site-footer {
    position: absolute; left: 0; top: 1142px; width: 745px; height: 58px;
    background: var(--footer); color: var(--white);
  }
  .footer-brand { position: absolute; left: 117px; top: 14px; font-size: 26px; font-weight: 800; line-height: 1; letter-spacing: 1px; }
  .footer-links { position: absolute; left: 360px; top: 23px; font-size: 9px; font-weight: 600; word-spacing: 2px; }
</style>
</head>
<body>
  <header class="hero" role="img" aria-label="City skyline above the clouds at sunrise">
  </header>
  <div class="nav-panel">
    <div class="brand">VR</div>
    <nav class="main-nav">
      <span>HOME</span><span>ABOUT US</span><span>CORPORATE GOVERNANCE</span><span>INVESTORS RELATIONS</span><span>PRESS</span><span>CONTACT</span>
    </nav>
  </div>
  <h1 class="hero-title">STRATEGY<br>DEVELOPMENT<br>PARTNERSHIP</h1>
  <div class="slider-dots"><span></span><span></span><span></span></div>

  <section class="pillar-band"></section>
  <div class="pillar pillar-vision" role="img" aria-label="Night city view behind the vision title">
    <h2>VISION</h2>
    <p>We aim to be the leading private investment group by the year 2030.</p>
  </div>
  <div class="pillar pillar-mission" role="img" aria-label="Business meeting behind the mission title">
    <h2>MISSION</h2>
  </div>
  <div class="pillar pillar-strategy" role="img" aria-label="Blue network globe behind the strategy title">
    <h2>STRATEGY</h2>
  </div>

  <section class="news-grid">
    <div class="tile photo-desert" role="img" aria-label="Camel caravan crossing desert dunes at sunset"></div>
    <article class="tile news-card news-card-top">
      <h3>NEWS HEADING</h3>
      <p>Our partners met this quarter to review new private holdings and long term growth plans for members across the region.</p>
      <div class="news-meta"><span>Read More</span><span>Share</span></div>
    </article>
    <div class="tile photo-road" role="img" aria-label="Open highway through green countryside"></div>
    <div class="tile photo-portrait" role="img" aria-label="Portrait of a businessman in a dark suit"></div>
    <article class="tile news-card news-card-mid">
      <h3>NEWS HEADING</h3>
      <p>A short update on recent acquisitions, member events and the outlook for the coming investment season.</p>
      <div class="news-meta"><span>Read More</span><span>Share</span></div>
    </article>
    <div class="tile photo-car" role="img" aria-label="Silver luxury sedan"></div>
    <div class="tile photo-night" role="img" aria-label="City street with light trails at night"></div>
    <div class="browse-bar">BROWSE ALL NEWS</div>
  </section>

  <footer class="site-footer">
    <div class="footer-brand">VR</div>
    <div class="footer-links">Privacy Policy &nbsp;|&nbsp; Terms &amp; Conditions &nbsp;|&nbsp; FAQs &nbsp;|&nbsp; Sitemap</div>
  </footer>
</body>
</html>
```